Home Design company focused on remodel and enhancement of kitchens and bathroorms

I already have a logo designed by ArtHarbor, I now need a design for my business cards.
The company is in the remodeling and enhancement industry for homes, focusing on kitchens and bathrooms, however, we can remodel or enhance every room in a home, an office space, etc.

The company's name is VELMOR HOME DESIGN, LLC

We'll focus on clients in the Rio Grande Valley, Texas. Primarily McAllen, Edinburg, Pharr, Mission, Brownsville and South Padre Island.

The design on the business card should transmit reliability, professionalism anda bit of upscale design.

The logo is in black and white, and would like to keep it that way.

The information that needs to be printed in the business cards is:
Company's name: Velmor Home Design
Company's Logo (attached)
My name: Noel Bramwit
Address, phone and email:
2715 N Parkline Road, Ste 348
Larkvale, TX 78599
(555) 010 0187
nbramwit@velmordesign.example
Website: velmordesign.example

```html
<!DOCTYPE html>
<html lang="en">
<head>
<meta charset="utf-8">
<title>Velmor Home Design — Business Cards</title>
<link rel="stylesheet" href="https://fonts.googleapis.com/css2?family=Montserrat:wght@400;500;600&display=swap">
<style>
  :root {
    --ink: #000000;
    --paper: #ffffff;
    --backdrop: #9d9e9f;
    --card-w: 361px;
    --card-h: 634px;
  }
  * { box-sizing: border-box; margin: 0; padding: 0; }
  html, body {
    width: 1200px;
    height: 900px;
    overflow: hidden;
  }
  body {
    background: var(--backdrop);
    font-family: "Montserrat", Arial, sans-serif;
    position: relative;
  }
  .card {
    position: absolute;
    top: 133px;
    width: var(--card-w);
    height: var(--card-h);
    overflow: hidden;
    background: var(--paper);
  }
  .card--front { left: 183px; }
  .card--back  { left: 656px; }
  .card__roof {
    position: absolute;
    inset: 0;
    width: 100%;
    height: 100%;
  }
  .wordmark {
    position: absolute;
    left: 0;
    right: 0;
    display: flex;
    justify-content: center;
    align-items: center;
    gap: 20px;
    color: var(--paper);
  }
  .wordmark__square {
    width: 40px;
    height: 40px;
    background: var(--paper);
  }
  .wordmark__name {
    font-weight: 500;
    font-size: 16px;
    line-height: 18px;
    letter-spacing: 0.26em;
    text-transform: uppercase;
  }
  .card--front .wordmark { top: 519px; }
  .card--back .wordmark { top: 54px; }
  .contact {
    position: absolute;
    left: 0;
    right: 0;
    text-align: center;
    color: var(--ink);
    font-style: normal;
  }
  .contact__name {
    top: 286px;
    font-weight: 600;
    font-size: 28px;
    letter-spacing: 0.06em;
    text-transform: uppercase;
  }
  .contact__address {
    top: 375px;
    font-size: 19px;
    line-height: 28px;
  }
  .contact__reach {
    top: 511px;
    font-size: 19px;
    line-height: 27px;
  }
  .contact p { white-space: nowrap; }
</style>
</head>
<body>

  <section class="card card--front" aria-label="Business card front">
    <svg class="card__roof" viewBox="0 0 361 634" preserveAspectRatio="none" aria-hidden="true">
      <polygon points="0,264 180.5,159 361,264 361,634 0,634" fill="var(--ink)"/>
    </svg>
    <div class="wordmark">
      <span class="wordmark__square"></span>
      <span class="wordmark__name">Velmor<br>Home<br>Design</span>
    </div>
  </section>

  <section class="card card--back" aria-label="Business card back">
    <svg class="card__roof" viewBox="0 0 361 634" preserveAspectRatio="none" aria-hidden="true">
      <polygon points="0,0 361,0 361,264 180.5,159 0,264" fill="var(--ink)"/>
    </svg>
    <div class="wordmark">
      <span class="wordmark__square"></span>
      <span class="wordmark__name">Velmor<br>Home<br>Design</span>
    </div>

    <h1 class="contact contact__name">Noel Bramwit</h1>

    <address class="contact contact__address">
      <p>2715 N Parkline Road</p>
      <p>Suite 348</p>
      <p>Larkvale, TX 78599</p>
    </address>

    <div class="contact contact__reach">
      <p>(555) 010 0187</p>
      <p>nbramwit@velmordesign.example</p>
      <p>www.velmordesign.example</p>
    </div>
  </section>

</body>
</html>
```